Business Card Design for Law firm - already have logo

Now that we have a logo, we need a business card design - our logo is attached -it is salaryman font if that helps - we would like a file that can be uploaded to kellumo (www.kellumo.com) using the logo and with the following information on it:
Dunmore Law Firm, P.C.
Felix Dunmore, Esq.
6718 NE 19th Ave.
Portland, OR 97284
971.555.0142 phone
971.555.0187 fax
fel@dunmore.net
Callnest: feldunmore
Chatwire: felix.dunmore@quillmail.com
Target Market(s)
our business cards are distributed to corporate executives, technology professionals and healthcare providers
Industry/Entity Type
Business
Look and feel

```html
<!DOCTYPE html>
<html lang="en">
<head>
<meta charset="utf-8">
<title>Dunmore Law Firm, P.C. — Business Card</title>
<link rel="stylesheet" href="https://fonts.googleapis.com/css2?family=Roboto+Condensed:wght@300;400;700&display=swap">
<style>
  :root {
    --backdrop: #e4e2df;
    --card: #ffffff;
    --ink: #0b0b0b;
    --ink-soft: #2a2a2a;
    --band-text: #ffffff;
    --texture-light: #3a3a3a;
    --texture-dark: #141414;
  }
  * { box-sizing: border-box; margin: 0; padding: 0; }
  html, body {
    width: 1200px;
    height: 864px;
    overflow: hidden;
    background: var(--backdrop);
  }
  body {
    position: relative;
    font-family: "Roboto Condensed", "Arial Narrow", sans-serif;
  }
  .business-card {
    position: absolute;
    left: 100px;
    top: 146px;
    width: 1000px;
    height: 572px;
    background: var(--card);
    box-shadow: 0 6px 22px rgba(0, 0, 0, 0.18);
    overflow: hidden;
  }
  .brand-band {
    position: absolute;
    left: 0;
    top: 22px;
    width: 100%;
    height: 112px;
    background: var(--ink);
    display: flex;
    align-items: center;
    padding-left: 30px;
  }
  .logo-slot {
    position: relative;
    width: 520px;
    height: 84px;
    display: flex;
    align-items: center;
    gap: 18px;
    padding-left: 26px;
  }
  .logo-texture {
    position: absolute;
    inset: 0;
    background: linear-gradient(100deg, var(--texture-dark) 0%, var(--texture-light) 45%, var(--texture-dark) 100%);
  }
  .logo-mark {
    position: relative;
    width: 30px;
    height: 30px;
    background: var(--band-text);
  }
  .brand-name {
    position: relative;
    color: var(--band-text);
    font-weight: 300;
    font-size: 58px;
    line-height: 1;
  }
  .contact-list {
    list-style: none;
    margin-left: 24px;
    color: var(--band-text);
    font-weight: 300;
    font-size: 22px;
    line-height: 1.3;
  }
  .contact-list b {
    font-weight: 700;
    margin-right: 4px;
  }
  .firm-details {
    position: absolute;
    left: 60px;
    top: 392px;
    color: var(--ink);
  }
  .firm-name {
    font-weight: 700;
    font-size: 36px;
    letter-spacing: 0.01em;
    text-transform: uppercase;
    line-height: 1.1;
  }
  .firm-address {
    margin-top: 8px;
    font-weight: 300;
    font-size: 29px;
    color: var(--ink-soft);
    line-height: 1.1;
  }
  .firm-address sup {
    font-size: 0.55em;
    vertical-align: super;
    line-height: 0;
  }
  .messaging-band {
    position: absolute;
    left: 0;
    top: 500px;
    width: 100%;
    height: 48px;
    background: var(--ink);
    color: var(--band-text);
    display: flex;
    align-items: center;
    padding-left: 60px;
    font-weight: 300;
    font-size: 24px;
  }
</style>
</head>
<body>
  <article class="business-card">
    <header class="brand-band">
      <div class="logo-slot">
        <span class="logo-texture" role="img" aria-label="Firm logo area with textured letter tiles"></span>
        <span class="logo-mark"></span>
        <span class="brand-name">Dunmore</span>
      </div>
      <ul class="contact-list">
        <li><b>P</b>971.555.0142</li>
        <li><b>F</b>971.555.0187</li>
        <li><b>E</b>fel@dunmore.net</li>
      </ul>
    </header>

    <section class="firm-details">
      <h1 class="firm-name">Dunmore Law Firm, P.C.</h1>
      <p class="firm-address">Felix Dunmore, Esq., 6718 NE 19<sup>th</sup> Ave., Portland, or 97284.</p>
    </section>

    <footer class="messaging-band">
      Callnest: feldunmore | Chatwire: felix.dunmore@quillmail.com
    </footer>
  </article>
</body>
</html>
```